Tinker's Ride 5, The fifth annual Tinker's Ride motorcycle event, www.tinkersride-example.com

We need an event poster that can be used in print and on the web to promote our event. Files for the poster should be modifiable to add additional information as it becomes available. The Tinker's Ride is a gathering for Vintage, Classic and Cafe' Racer motorcycles and their riders, Rockers and Mods. The event date is Saturday, July 26, 2014, rain or shine, from 9:00 AM to 6:00 PM EDT at Welden Park, 217 North Birch Avenue, Pittston, PA 18640 USA. Friday July 25 Meet and Greet from 7:00 PM to close at Hadley's Hideaway, Pittston, PA. Stragglers' Brunch, Sunday, July 27, 7:00 to 10:00 AM, location tba. Optional Group Ride Saturday from 10:00 AM to Noon. Varlo 450 Custom Cafe' Motorcycle Raffle, Contests, Trophies and Cash Prizes for Pin-up Girl, Coolest Cafe' Racer Motorcycle, Coolest Mod Scooter, Peoples Choice Motorcycle, and More! Live music by the one and only legendary TKWZ, "Slim Jim" Orvo and more tba. Brought to you by Valtor Riders, www.facebook.com/valtorriders?ref=hl, Brindle and Moss/Moss Ruffians, www.brindleandmoss-example.com. Partial Proceeds to benefit the KWLTS and The Upper Valley Rescue Squad Society. More information and advance tickets available at www.tinkersride-example.com
Uploaded files include: Valtor Riders Logo, Moss Ruffian's Logo, stock vintage image, two images from 2014 event, and a photo of the bike to be raffled (better image in the works.

Thank you to all who participated in our competition.  We received excellent work from you all, and the hard part for us is having to choose.  Our decision will be made today.

```html
<!DOCTYPE html>
<html lang="en">
<head>
<meta charset="utf-8">
<title>Tinker's Ride 5 – Event Poster</title>
<link href="https://fonts.googleapis.com/css2?family=Righteous&family=Abril+Fatface&family=Indie+Flower&family=Oswald:wght@400;500&family=Arimo:wght@400;700&display=swap" rel="stylesheet">
<style>
  :root {
    --page-bg: #e4eaea;
    --poster-bg: #1e1d1c;
    --flame-deep: #7a2406;
    --flame-hot: #f08a1c;
    --flame-light: #ffd36b;
    --wood-dark: #8a5a24;
    --wood-mid: #b98542;
    --wood-light: #d4a35c;
    --text-white: #ffffff;
    --day-red: #c4160f;
    --prize-gold: #e2cf7a;
    --band-dark: #1a1a1a;
    --band-maroon: #5a1412;
    --footer-light: #f4f5f5;
    --footer-mid: #c9cccc;
    --ticket-olive: #9a9a2a;
    --footer-ink: #1b1b1b;
  }
  * { margin: 0; padding: 0; box-sizing: border-box; }
  html, body { width: 1200px; height: 1000px; overflow: hidden; }
  body { background: var(--page-bg); position: relative; }

  .poster {
    position: absolute; left: 302px; top: 35px;
    width: 560px; height: 928px;
    background: radial-gradient(ellipse at 50% 60%, #2b2a28 0%, var(--poster-bg) 70%);
    overflow: hidden;
  }
  .flames {
    position: absolute; inset: 0;
    background:
      radial-gradient(ellipse 70% 22% at 60% 14%, var(--flame-light) 0%, var(--flame-hot) 35%, rgba(122,36,6,0.6) 65%, transparent 80%),
      radial-gradient(ellipse 30% 30% at 98% 35%, var(--flame-hot) 0%, rgba(122,36,6,0.5) 55%, transparent 75%),
      radial-gradient(ellipse 22% 20% at 0% 62%, var(--flame-hot) 0%, rgba(122,36,6,0.5) 55%, transparent 80%),
      radial-gradient(ellipse 35% 14% at 8% 68%, rgba(240,138,28,0.8) 0%, transparent 75%);
  }
  .presenter {
    position: absolute; left: 12px; top: 12px;
    font-family: "Arimo", sans-serif; font-size: 19px; color: var(--text-white);
  }
  .title { position: absolute; left: 0; top: 70px; width: 560px; height: 120px; }
  .title text { font-family: "Righteous", sans-serif; }
  .anniversary {
    position: absolute; left: 0; top: 160px; width: 560px; text-align: center;
    font-family: "Abril Fatface", serif; font-size: 40px; color: #e8e8e8;
    letter-spacing: 1px; text-shadow: 2px 2px 0 #333;
  }
  .anniversary sup { font-size: 18px; vertical-align: 22px; }

  .schedule {
    position: absolute; left: 16px; top: 232px; width: 528px; height: 346px;
    background:
      repeating-linear-gradient(178deg, rgba(0,0,0,0.06) 0 3px, transparent 3px 9px),
      linear-gradient(180deg, var(--wood-light), var(--wood-mid) 50%, var(--wood-dark));
    box-shadow: inset 0 0 14px rgba(0,0,0,0.7), 0 0 6px rgba(0,0,0,0.8);
    border-radius: 4px;
    font-family: "Indie Flower", cursive; font-size: 17px; color: var(--text-white);
    text-shadow: 1px 1px 1px #2a1a08;
    text-align: center; padding-top: 28px;
  }
  .schedule p { line-height: 22px; margin-bottom: 22px; }
  .schedule .day { color: var(--day-red); font-size: 21px; text-shadow: 1px 1px 0 #3a0e05; }

  .prizes {
    position: absolute; left: 18px; top: 612px;
    font-family: "Oswald", sans-serif; color: var(--prize-gold);
    text-shadow: 1px 1px 1px #000;
  }
  .prizes h3 { font-size: 12px; font-weight: 500; margin-bottom: 6px; }
  .prizes li { list-style: none; font-size: 16px; line-height: 33px; }

  .live-plaque {
    position: absolute; left: 310px; top: 600px; width: 218px; height: 63px;
    background: linear-gradient(180deg, var(--wood-light), var(--wood-dark));
    box-shadow: inset 0 0 10px rgba(0,0,0,0.8);
    border-radius: 4px;
    font-family: "Oswald", sans-serif; text-align: center; line-height: 63px;
  }
  .live-plaque .live { font-size: 38px; color: var(--band-maroon); font-weight: 500; }
  .live-plaque .event { font-size: 20px; color: var(--prize-gold); }
  .lineup {
    position: absolute; left: 290px; top: 672px; width: 258px; text-align: center;
    font-family: "Arimo", sans-serif; font-weight: 700;
  }
  .lineup .headliner { font-size: 50px; color: var(--band-dark); text-shadow: 0 0 2px #555; line-height: 58px; }
  .lineup .support { font-size: 23px; color: var(--band-maroon); line-height: 30px; }
  .lineup .tba { font-size: 23px; color: var(--text-white); line-height: 36px; }

  .footer {
    position: absolute; left: 0; bottom: 0; width: 560px; height: 70px;
    background: linear-gradient(180deg, var(--footer-light), var(--footer-mid));
    border-top: 3px solid #9a9a9a;
    display: flex; align-items: center; padding: 0 12px;
    font-family: "Arimo", sans-serif; color: var(--footer-ink);
  }
  .sponsor { display: flex; align-items: center; gap: 5px; font-size: 13px; font-weight: 700; margin-right: 14px; }
  .sponsor .mark { width: 16px; height: 16px; border-radius: 50%; background: var(--footer-ink); }
  .tickets { margin-left: auto; text-align: right; font-size: 17px; line-height: 22px; }
  .tickets .hl { color: var(--ticket-olive); }
</style>
</head>
<body>
  <main class="poster">
    <div class="flames" role="img" aria-label="Roaring fire flames around the title and down the sides"></div>

    <p class="presenter">Valtor Riders Present:</p>

    <svg class="title" viewBox="0 0 560 120" aria-label="The Tinker's Ride">
      <defs>
        <path id="title-arc" d="M30 112 Q280 38 530 112"/>
        <linearGradient id="title-fill" x1="0" y1="0" x2="0" y2="1">
          <stop offset="0" stop-color="#fbf3b0"/>
          <stop offset="1" stop-color="#7b8a2a"/>
        </linearGradient>
      </defs>
      <text font-size="42" fill="url(#title-fill)" stroke="#1a1a1a" stroke-width="1.5" text-anchor="middle">
        <textPath href="#title-arc" startOffset="50%">THE TINKER'S RIDE</textPath>
      </text>
    </svg>

    <h2 class="anniversary">5<sup>TH</sup> ANNIVERSARY</h2>

    <section class="schedule" role="img" aria-label="Wood plank board with event schedule">
      <p><span class="day">Friday</span> July 25 Meet and Greet from 7:00 PM</p>
      <p>(to close at Hadley's Hideaway, Pittston, PA. Stragglers' Brunch)</p>
      <p><span class="day">Saturday</span>, July 26, 2014, from 9:00 AM to 6:00 PM EDT</p>
      <p>(Welden Park, 217 North Birch Avenue, Pittston, PA 18640 USA)</p>
      <p>Optional Group Ride Saturday from 10:00 AM to Noon</p>
      <p><span class="day">Sunday</span>, July 27, 7:00 to 10:00 AM,</p>
      <p>(location tba)</p>
    </section>

    <section class="prizes">
      <h3>Contests, Trophies and Cash Prizes for:</h3>
      <ul>
        <li>-Pin-up Girl,</li>
        <li>-Coolest Cafe' Racer Motorcycle,</li>
        <li>-Coolest Mod Scooter,</li>
        <li>-Peoples Choice Motorcycle,</li>
        <li>....... and More!</li>
      </ul>
    </section>

    <div class="live-plaque"><span class="live">LIVE</span> <span class="event">event:</span></div>
    <section class="lineup">
      <p class="headliner">TKWZ</p>
      <p class="support">"Slim Jim" Orvo</p>
      <p class="tba">tba...</p>
    </section>

    <footer class="footer">
      <div class="sponsor"><span class="mark"></span>Valtor Riders</div>
      <div class="sponsor">Moss Ruffian's</div>
      <div class="sponsor">KWLTS</div>
      <div class="tickets"><span class="hl">Tickets</span> available at:<br>www.tinkersride-example.com</div>
    </footer>
  </main>
</body>
</html>
```